Business Card Design Project - The Kernel Harbor

Company Name - The Kernel Harbor

We need a unique logo and business cards

We are a team of experienced IT professionals who specialize in providing business value to organizations via the analysis and understanding the challenges of your particular organization. We focus on understanding the challenges first, and execute against your priorities partnering with your highly valued key resources.

Our extensive experience and focus on Agile delivery methodologies help our clients continuously improve and deliver quality solutions. Using this approach we will always deliver the greatest return on your investments.

Target Market(s)

Large organizations IT departments

Industry/Entity Type

Business

Font styles to use
Serif
Sans Serif

Requirements
Should not have
• no pictures

```html
<!DOCTYPE html>
<html lang="en">
<head>
<meta charset="utf-8">
<title>The Kernel Harbor — Business Cards</title>
<link rel="stylesheet" href="https://fonts.googleapis.com/css2?family=Questrial&display=swap">
<style>
  :root {
    --backdrop: #2c2c2e;
    --card-white: #f7f7f7;
    --brand-red: #e01f26;
    --brand-blue: #3a6db5;
    --ink: #222222;
    --paper-line: #ffffff;
  }
  * { box-sizing: border-box; margin: 0; padding: 0; }
  html, body {
    width: 1200px; height: 1000px; overflow: hidden;
    background: var(--backdrop);
    font-family: "Questrial", sans-serif;
  }
  .card {
    position: absolute; left: 220px;
    width: 760px; height: 434px;
    background: var(--card-white);
    overflow: hidden;
    box-shadow: 0 14px 30px rgba(0,0,0,.45);
  }
  .card--front { top: 40px; }
  .card--back { top: 526px; }
  .card-shapes { position: absolute; inset: 0; }
  .wordmark {
    position: absolute;
    display: flex; align-items: center; gap: 14px;
    color: var(--ink);
    font-size: 34px; letter-spacing: 3px;
    white-space: nowrap;
  }
  .wordmark-dot {
    width: 22px; height: 22px; border-radius: 50%;
    background: var(--brand-red);
  }
  .card--front .wordmark { left: 0; right: 0; top: 120px; justify-content: center; }
  .card--back .wordmark { left: 46px; top: 100px; font-size: 30px; }
  .front-web {
    position: absolute; left: 40px; top: 266px;
    color: #fff; font-size: 26px; letter-spacing: 1.5px;
  }
  .holder {
    position: absolute; left: 576px; top: 116px;
    width: 164px; color: #fff; text-align: right;
    white-space: nowrap;
  }
  .holder-name { font-size: 22px; line-height: 26px; }
  .holder-role { font-size: 14px; line-height: 18px; }
  .contact-list {
    position: absolute; left: 50px; top: 256px;
    list-style: none; color: #fff; font-size: 22px; letter-spacing: .5px;
  }
  .contact-list li { display: flex; align-items: center; gap: 12px; height: 36px; white-space: nowrap; }
  .contact-list svg { width: 20px; height: 20px; flex: none; }
</style>
</head>
<body>

<section class="card card--front" aria-label="Card front">
  <svg class="card-shapes" viewBox="0 0 760 434" aria-hidden="true">
    <rect x="0" y="250" width="760" height="184" fill="var(--brand-blue)"/>
    <path d="M-4 244 H620 a38 38 0 0 1 0 76 H-4 Z" fill="var(--brand-red)" stroke="var(--paper-line)" stroke-width="4"/>
  </svg>
  <div class="wordmark"><span class="wordmark-dot"></span>The Kernel Harbor</div>
  <p class="front-web">www.kernelharbor.com</p>
</section>

<section class="card card--back" aria-label="Card back">
  <svg class="card-shapes" viewBox="0 0 760 434" aria-hidden="true">
    <rect x="500" y="0" width="260" height="434" fill="var(--brand-red)"/>
    <rect x="0" y="410" width="760" height="24" fill="var(--brand-red)"/>
    <line x1="520" y1="198" x2="762" y2="176" stroke="var(--paper-line)" stroke-width="4"/>
    <path d="M-4 236 H560 a90 90 0 0 1 90 90 V414 H-4 Z" fill="var(--brand-blue)" stroke="var(--paper-line)" stroke-width="4"/>
  </svg>
  <svg class="card-shapes" viewBox="0 0 760 434" role="img" aria-label="Portrait placeholder">
    <circle cx="520" cy="180" r="44" fill="var(--brand-red)" stroke="var(--paper-line)" stroke-width="4"/>
  </svg>
  <div class="wordmark"><span class="wordmark-dot"></span>The Kernel Harbor</div>
  <div class="holder">
    <p class="holder-name">Your Sir Name</p>
    <p class="holder-role">Manager</p>
  </div>
  <ul class="contact-list">
    <li>
      <svg viewBox="0 0 20 20" aria-hidden="true"><rect x="2" y="4" width="16" height="12" fill="#fff"/><path d="M2 4 L10 11 L18 4" fill="none" stroke="var(--brand-blue)" stroke-width="1.6"/></svg>
      admin@kernelharbor.com
    </li>
    <li>
      <svg viewBox="0 0 20 20" aria-hidden="true"><path d="M10 2 a6 6 0 0 1 6 6 c0 5 -6 10 -6 10 s-6 -5 -6 -10 a6 6 0 0 1 6 -6 Z" fill="#fff"/><circle cx="10" cy="8" r="2.2" fill="var(--brand-blue)"/></svg>
      PO Box 4180, Bayview, CA
    </li>
    <li>
      <svg viewBox="0 0 20 20" aria-hidden="true"><path d="M5 2 h3 l1 4 -2 2 a10 10 0 0 0 5 5 l2 -2 4 1 v3 a2 2 0 0 1 -2 2 A15 15 0 0 1 3 4 a2 2 0 0 1 2 -2 Z" fill="#fff"/></svg>
      555-014-2286
    </li>
    <li>
      <svg viewBox="0 0 20 20" aria-hidden="true"><rect x="2" y="3" width="16" height="11" rx="1" fill="none" stroke="#fff" stroke-width="2"/><rect x="7" y="16" width="6" height="2" fill="#fff"/></svg>
      www.kernelharbor.com
    </li>
  </ul>
</section>

</body>
</html>
```